IT-Dienstleister für Projektmanagementsoftware sucht Broschüre im DIN-A4-Format
Zielgruppe
Wir sind ein IT-Dienstleister für Projektmanagementsoftware. Wir installieren, migrieren und entwickeln Software für das Projektmanagement auf Basis von Veltrano Technologien. Unsere Zielgruppe sind mittelständische Unternehmen und große Konzerne. Je komplexer das Projektmanagement in einem Unternehmen, desto eher helfen unsere Lösungen.
Aufgabenstellung
Es soll eine DIN A4 Hochglanz Broschüre für eine Messe entstehen. Wir haben bereits ein Grobkonzept mit Bildauswahl und Texten erstellt. An diesem soll sich orientiert werden. Bezüglich desDesigns, der Anordnung der Texte und Bilder etc. besteht völlige Freiheit. Weitere Orientierung bieten unsere Webseiten haldewiegand.de und quilbyte.de. Die Texte und Screenshots sind teilweise nur Platzhalter und müssen später noch angepasst werden können. Wir benötigen daher unbedingt die Rohdaten des Designs.

```html
<!DOCTYPE html>
<html lang="de">
<head>
<meta charset="utf-8">
<title>Produktbroschüre – Projektmanagement-Lösungen</title>
<link href="https://fonts.googleapis.com/css2?family=Roboto:wght@300;400;500;700&display=swap" rel="stylesheet">
<style>
  :root {
    --backdrop: #d9d9dc;
    --divider: #ffffff;
    --brand-green: #8dc02f;
    --page-grey: #eeeeee;
    --sheet: #ffffff;
    --ink: #333333;
    --ink-soft: #777777;
    --rule: #c8c8c8;
  }
  * { box-sizing: border-box; margin: 0; padding: 0; }
  html, body { width: 1200px; height: 3551px; overflow: hidden; }
  body {
    position: relative;
    background: var(--backdrop);
    font-family: 'Roboto', Arial, sans-serif;
    color: var(--ink);
  }
  .spread {
    position: absolute;
    left: 0;
    width: 1200px;
    height: 877px;
    background: var(--backdrop);
  }
  .spread + .spread { border-top: 14px solid var(--divider); }
  .spread--elk    { top: 0; }
  .spread--falcon { top: 877px; height: 891px; }
  .spread--heron  { top: 1768px; height: 891px; }
  .spread--lynx   { top: 2659px; height: 892px; }

  .page {
    position: absolute;
    top: 96px;
    height: 685px;
  }
  .page--cover { left: 127px; width: 470px; overflow: hidden; }
  .page--detail { left: 597px; width: 481px; background: var(--page-grey); }

  .cover-photo { position: absolute; left: 0; top: 0; width: 470px; height: 420px; }
  .cover-band { position: absolute; left: 0; top: 0; width: 470px; height: 685px; }

  .cover-text { position: absolute; left: 50px; right: 118px; color: #fff; }
  .cover-title { top: 408px; font-size: 40px; font-weight: 300; letter-spacing: .2px; white-space: nowrap; right: 40px; }
  .cover-lead { top: 466px; font-size: 13px; font-weight: 300; line-height: 1.3; color: #f1f8e2; right: 40px; }
  .cover-body { top: 520px; font-size: 8.4px; line-height: 1.5; color: #f6fbec; }
  .cover-body p + p { margin-top: 10px; }
  .cover-body .feature-head { font-weight: 700; margin-top: 12px; }
  .cover-body .feature-item { padding-left: 10px; }

  .detail-sheet {
    position: absolute;
    left: 44px; top: 48px;
    width: 393px; height: 575px;
    background: var(--sheet);
    box-shadow: 0 1px 4px rgba(0,0,0,.12);
  }
  .shot {
    position: absolute;
    left: 14px; width: 365px;
    background: linear-gradient(180deg, #f3f4f6 0%, #e6e8eb 100%);
    border: 1px solid #dcdfe3;
  }
  .diagram-area {
    position: absolute;
    left: 14px; width: 365px;
    background: linear-gradient(135deg, #f4f9ea 0%, #e3efcc 100%);
  }
  .feature-list {
    position: absolute;
    left: 14px; right: 18px;
    list-style: none;
    font-size: 8.4px;
    line-height: 1.45;
    color: var(--ink);
  }
  .feature-list li { position: relative; padding-left: 12px; margin-bottom: 6px; }
  .feature-list li::before {
    content: "»"; position: absolute; left: 0; top: 0; color: var(--ink-soft);
  }
  .feature-list b { font-weight: 700; }
  .list-rule { position: absolute; left: 14px; width: 175px; border-top: 1px solid var(--rule); }
</style>
</head>
<body>

<section class="spread spread--elk">
  <article class="page page--cover">
    <div class="cover-photo" role="img" aria-label="Titelfoto: Braunbär im Porträt vor dunklem Waldhintergrund" style="background: linear-gradient(160deg, #3c4436 0%, #6b5440 45%, #8a6446 70%, #4e4236 100%);"></div>
    <svg class="cover-band" viewBox="0 0 470 685" aria-hidden="true"><polygon points="0,358 470,392 470,685 0,685" fill="var(--brand-green)"/></svg>
    <h1 class="cover-text cover-title">Mighty Elk</h1>
    <p class="cover-text cover-lead">Einfaches planen und steuern großer Projekt-<br>portfolios und komplexer Programme</p>
    <div class="cover-text cover-body">
      <p>Mighty Elk ist die Lösung für ein erfolgreiches Projekt-, Programm- und Portfoliomanagement, welche technisch auf Veltrano Planner Server/Online basiert. Das zukunftsorientierte Tool hilft großen Unternehmen bei der Planung und Steuerung ihrer Projekte.</p>
      <p>Mighty Elk aggregiert Projektinformationen auf verschiedenen Ebenen und ermöglicht eine Kollaboration und Eskalation zwischen Projekten und unterschiedlichen Hierarchieebenen.</p>
    </div>
  </article>
  <article class="page page--detail">
    <div class="detail-sheet">
      <div class="diagram-area" style="top: 18px; height: 200px;" role="img" aria-label="Grafik: Pyramide aus Portfolio-, Programm- und Projektmanagement neben ineinandergreifenden Zahnrädern"></div>
      <div class="diagram-area" style="top: 236px; height: 196px;" role="img" aria-label="Grafik: Positionierung zwischen Standardisierung und Individualisierung mit Optimum-Stern"></div>
      <ul class="feature-list" style="top: 448px;">
        <li><b>Ganzheitliche Steuerung</b> auf Projekt-, Programm- und Portfolioebene</li>
        <li><b>Portfoliomanagement:</b> Qualifizierte Auswahl der richtigen Anforderungen, Genehmigung der Projekte sowie effiziente Steuerung der Umsetzung</li>
        <li><b>Programmmanagement:</b> Planung und Steuerung der Programme sowie Abgleich mit den dazugehörigen Projekten</li>
        <li><b>Projektmanagement:</b> Initiieren, Planen, Controllen/Steuern und Abschließen von Einzel-Projekten</li>
      </ul>
    </div>
  </article>
</section>

<section class="spread spread--falcon">
  <article class="page page--cover">
    <div class="cover-photo" role="img" aria-label="Titelfoto: Löwe mit Mähne vor dunklem Hintergrund" style="background: linear-gradient(160deg, #1e1a1a 0%, #5a3a22 40%, #a06a34 60%, #3a2a20 100%);"></div>
    <svg class="cover-band" viewBox="0 0 470 685" aria-hidden="true"><polygon points="0,362 470,378 470,685 0,685" fill="var(--brand-green)"/></svg>
    <h1 class="cover-text cover-title">Great Falcon</h1>
    <p class="cover-text cover-lead">Einfache und transparente Projektabbildung<br>und -abwicklung in TeamNexus</p>
    <div class="cover-text cover-body">
      <p>Great Falcon erweitert den bestehenden Standard-Funktionsumfang von Veltrano TeamNexus um Fähigkeiten für ein echtes Multiprojektmanagement.</p>
      <p>Im Fokus stehen dabei Bedienbarkeit, Echtzeit-Controlling und Kosteneffizienz. Great Falcon ist die optimale Lösung für die professionelle Projektverwaltung von mittleren und großen Unternehmen.</p>
    </div>
  </article>
  <article class="page page--detail">
    <div class="detail-sheet">
      <div class="shot" style="top: 16px; height: 182px;" role="img" aria-label="Bildschirmansicht Projekt Center mit Projektbaum und Statusampeln"></div>
      <div class="shot" style="top: 204px; height: 124px;" role="img" aria-label="Bildschirmansicht Projektdetails mit Tabellen zu Teilprojekten, Problemen und Risiken"></div>
      <ul class="feature-list" style="top: 352px;">
        <li><b>Projekt Center:</b> aggregierte Übersicht zur einfachen Darstellung wesentlicher Statusinformationen aller Projekte – alle Projekte und Ressourcen im Blick</li>
        <li><b>Projektanlage:</b> über benutzerfreundliches und dynamisches Formular – problemlose Navigation zwischen Projekt Center und Projektarbeitsbereich möglich</li>
        <li><b>Phasenansicht:</b> Überblick über alle wesentlichen Projektaufgaben, direkte Verknüpfung mit Aufgabenliste, Kombination aus Phasen- und Ganttansicht ermöglicht schnelle Einordnung des Projektstatus</li>
      </ul>
      <div class="list-rule" style="top: 474px;"></div>
      <ul class="feature-list" style="top: 489px;">
        <li>schnelle Transparenz</li>
        <li>einfach und transparent</li>
        <li>für mittelgroße und große Unternehmen</li>
        <li>Ready To use</li>
      </ul>
    </div>
  </article>
</section>

<section class="spread spread--heron">
  <article class="page page--cover">
    <div class="cover-photo" role="img" aria-label="Titelfoto: Hochlandrind mit langen Hörnern in Graslandschaft unter bewölktem Himmel" style="background: linear-gradient(180deg, #5d6d7c 0%, #9aa6ae 35%, #6a4a30 65%, #8a7a5a 100%);"></div>
    <svg class="cover-band" viewBox="0 0 470 685" aria-hidden="true"><polygon points="0,365 470,392 470,685 0,685" fill="var(--brand-green)"/></svg>
    <h1 class="cover-text cover-title">Calm Heron</h1>
    <p class="cover-text cover-lead">Digitalisierung Ihres&nbsp; Ressourcengenehmigungs-<br>prozess in Veltrano Planner</p>
    <div class="cover-text cover-body">
      <p>Calm Heron unterstützt die Kommunikation zwischen Ressourcenmanagern und Projektleitern in Ihrem Unternehmen, indem es den Bedarf und die Freigabe an Ressourcen zentral und unabhängig verwaltet und so mögliche Abweichungen transparent abbildet.</p>
      <p>Mit Calm Heron bieten wir eine voll in den Planner Server integrierte Lösung zur Digitalisierung Ihres Ressourcenfreigabeprozesses. Profitieren Sie außerdem von der Integration von Calm Heron per Add-In in Ihr VT Planner Professional. So haben Sie Ihre Planung und Freigabe auch in Ihrem Client.</p>
    </div>
  </article>
  <article class="page page--detail">
    <div class="detail-sheet">
      <div class="shot" style="top: 14px; height: 168px;" role="img" aria-label="Bildschirmansicht Ressourcenanfrage mit geöffnetem Dialogfenster"></div>
      <div class="shot" style="top: 190px; height: 208px;" role="img" aria-label="Bildschirmansicht Ressourcenfreigabe mit Zeitraster und Freigabedialog"></div>
      <ul class="feature-list" style="top: 445px;">
        <li>Verbesserung der Kommunikation zwischen Ressourcenmanagern und Projektleitern</li>
        <li>Transparente Abbildung von Ressourcenabweichungen</li>
        <li>Digitalisierung des Ressourcenfreigabeprozesses</li>
        <li>Volle Planner Server Integration</li>
      </ul>
    </div>
  </article>
</section>

<section class="spread spread--lynx">
  <article class="page page--cover">
    <div class="cover-photo" role="img" aria-label="Titelfoto: gemusterte Schlange auf Ästen" style="background: linear-gradient(160deg, #6a5a48 0%, #a08c74 35%, #7a6a56 60%, #b8a88c 100%);"></div>
    <svg class="cover-band" viewBox="0 0 470 685" aria-hidden="true"><polygon points="0,372 470,392 470,685 0,685" fill="var(--brand-green)"/></svg>
    <h1 class="cover-text cover-title">Careful Lynx</h1>
    <p class="cover-text cover-lead">Risiko- und Issueportfolio übersichtlich dargestellt.</p>
    <div class="cover-text cover-body">
      <p>Careful Lynx dient zur grafischen und tabellerischen Aufbereitung des Risiko- und Issueportfolios. Damit werden kritische Zustände in Ihren Projekten noch schneller erkannt. Risiken und Issues können so spezifisch adressiert werden.</p>
      <p class="feature-head">Features</p>
      <p class="feature-item" style="margin-top:2px;">» On-Premise oder Cloud | Webbasierte Anwendung</p>
    </div>
  </article>
  <article class="page page--detail">
    <div class="detail-sheet">
      <div class="shot" style="top: 14px; height: 222px;" role="img" aria-label="Bildschirmansicht Risk Matrix mit farbiger Risikomatrix und Risikotabelle"></div>
      <div class="shot" style="top: 250px; height: 170px;" role="img" aria-label="Bildschirmansicht Issue Matrix mit farbiger Matrix und Issuetabelle"></div>
      <ul class="feature-list" style="top: 450px;">
        <li>Überblick über das gesamte Risiko- und Issueportfolio</li>
        <li>Click-to-Filter-Möglichkeit in der Matrix</li>
        <li>Export nach Tabulo</li>
        <li>Risk-to-Issue-Eskalation</li>
        <li>Interaktive Handhabung der Benutzeroberfläche</li>
        <li>Beziehung zwischen Risks und Issues</li>
      </ul>
    </div>
  </article>
</section>

</body>
</html>
```